Pebble Fold

Text is below. 4x6 single sided is fine (web flyer).
I don't have a firm idea for the design but I want it to have a spring fresh feel to it since the weather is getting nice. Light colors would be nice. A non-slutty girl is always good too, it's more of a professional house music type function. I attached my logo and the old flyer (not very good, just attached for the cork den logo) and some other flyers that I've chosen through artflock. You can start with the background/image and PEBBLE FOLD and add the text in later if you want to save time so I can tell you if I like the idea first. Thanks!
The Lanterns Reel presents
PEBBLE FOLD
WEDNESDAY 4/17/13
530-9PM
DECOMPRESS. INVIGORATE. REJUVENATE
Inside CORK DEN (logo)
Join resident deejay MILES HARTWICK (sociallink.example/lanternsreel) along with special guest this week:
QUILLON (Special UK Garage Set starting at 630pm) (logo)
(sociallink.example/quillon42)
PEBBLE FOLD is a weekly after-work chill-out lounge event for professionals, and sharp movers & shakers with sophisticated musical tastes.
Target Market(s)
Professionals and house music lovers, lounge atmosphere
Industry/Entity Type
House

```html
<!DOCTYPE html>
<html lang="en">
<head>
<meta charset="utf-8">
<title>Pebble Fold – Wednesday 17th April, 2013</title>
<link rel="stylesheet" href="https://fonts.googleapis.com/css2?family=Uncial+Antiqua&family=Libre+Baskerville:ital@0;1&family=Josefin+Sans:wght@600;700&family=Arimo:wght@400;700&display=swap">
<style>
  :root {
    --board: #2a2a2a;
    --board-light: #3a3a3a;
    --date-yellow: #f4ea2a;
    --ribbon-light: #f6cf86;
    --ribbon-dark: #e67422;
    --presenter-navy: #2a2f7a;
    --title-ink: #1d1a18;
    --time-white: #f4f1ea;
    --frame-cream: #fbf6dc;
    --tagline-green: #b9d53a;
    --info-blue: #a9dbe4;
    --dj-yellow: #f6ec2c;
    --rule: #151515;
    --venue-pink: #c13a78;
  }
  * { margin: 0; padding: 0; box-sizing: border-box; }
  html, body { width: 831px; height: 1200px; overflow: hidden; background: #ffffff; }
  .flyer {
    position: relative;
    width: 831px;
    height: 1200px;
    overflow: hidden;
    background: radial-gradient(ellipse at 50% 45%, var(--board-light) 0%, var(--board) 70%, #222 100%);
  }
  .event-date {
    position: absolute; left: 19px; top: 24px;
    font-family: "Uncial Antiqua", serif;
    font-size: 40px; color: var(--date-yellow);
    white-space: nowrap;
  }
  .title-ribbon { position: absolute; left: 0; top: 96px; width: 700px; height: 138px; }
  .presenter {
    position: absolute; left: 18px; top: 103px;
    font-family: "Libre Baskerville", serif; font-style: italic;
    font-size: 27px; color: var(--presenter-navy); white-space: nowrap;
  }
  .presenter small { font-style: normal; font-size: 17px; }
  .event-name {
    position: absolute; left: 16px; top: 145px;
    font-family: "Josefin Sans", sans-serif; font-weight: 700;
    font-size: 78px; line-height: 1; letter-spacing: 1px;
    color: var(--title-ink); white-space: nowrap;
  }
  .event-time {
    position: absolute; left: 19px; top: 250px;
    font-family: "Libre Baskerville", serif;
    font-size: 33px; color: var(--time-white); white-space: nowrap;
  }
  .feature-frame { position: absolute; left: 184px; top: 326px; width: 518px; height: 502px; }
  .tagline {
    position: absolute; left: 0; width: 831px; top: 882px; text-align: center;
    font-family: "Josefin Sans", sans-serif; font-weight: 700;
    font-size: 33px; color: var(--tagline-green); white-space: nowrap;
  }
  .rule { position: absolute; left: 111px; width: 644px; height: 2px; background: var(--rule); }
  .rule-top { top: 935px; }
  .rule-bottom { top: 1052px; }
  .resident {
    position: absolute; left: 0; width: 831px; top: 952px; text-align: center;
    font-family: "Arimo", sans-serif; font-size: 28px; color: var(--info-blue); white-space: nowrap;
  }
  .resident .dj-name { font-size: 43px; color: var(--dj-yellow); }
  .resident-link {
    position: absolute; left: 0; width: 831px; top: 1002px; text-align: center;
    font-family: "Arimo", sans-serif; font-size: 28px; color: var(--info-blue); white-space: nowrap;
  }
  .guest-name {
    position: absolute; left: 30px; top: 1093px;
    font-family: "Arimo", sans-serif; font-weight: 700;
    font-size: 32px; color: #ffffff; letter-spacing: 1px;
  }
  .guest-details {
    position: absolute; left: 30px; top: 1140px;
    font-family: "Arimo", sans-serif; font-size: 18px; line-height: 24px; color: #ffffff;
  }
  .venue {
    position: absolute; right: 14px; top: 1132px;
    display: flex; align-items: center; gap: 8px;
    font-family: "Arimo", sans-serif; font-weight: 400;
    font-size: 28px; color: var(--venue-pink); letter-spacing: 2px;
  }
  .venue-dot { width: 14px; height: 14px; border-radius: 50%; background: var(--venue-pink); }
</style>
</head>
<body>
<main class="flyer">
  <h2 class="event-date">Wednesday 17th April, 2013</h2>

  <svg class="title-ribbon" viewBox="0 0 700 138" aria-hidden="true">
    <defs>
      <linearGradient id="ribbonFill" x1="0" y1="0" x2="1" y2="0">
        <stop offset="0" stop-color="var(--ribbon-light)"/>
        <stop offset="1" stop-color="var(--ribbon-dark)"/>
      </linearGradient>
    </defs>
    <polygon points="0,0 700,0 643,69 700,138 0,138" fill="url(#ribbonFill)"/>
  </svg>
  <p class="presenter">The Lanterns Reel <small>presents</small></p>
  <h1 class="event-name">PEBBLE FOLD</h1>

  <p class="event-time">5.30 pm to 9.00 pm</p>

  <svg class="feature-frame" viewBox="0 0 570 575" preserveAspectRatio="none" role="img" aria-label="Photo of a female DJ in a black jacket holding sparkly headphones to her ears">
    <defs>
      <radialGradient id="photoTone" cx="0.5" cy="0.45" r="0.6">
        <stop offset="0" stop-color="#4a403a"/>
        <stop offset="0.6" stop-color="#1c1a19"/>
        <stop offset="1" stop-color="#0c0c0c"/>
      </radialGradient>
    </defs>
    <g fill="var(--frame-cream)">
      <circle cx="285" cy="287" r="258"/>
      <circle cx="285" cy="55" r="30"/><circle cx="345" cy="63" r="30"/><circle cx="401" cy="86" r="30"/>
      <circle cx="449" cy="123" r="30"/><circle cx="486" cy="171" r="30"/><circle cx="509" cy="227" r="30"/>
      <circle cx="517" cy="287" r="30"/><circle cx="509" cy="347" r="30"/><circle cx="486" cy="403" r="30"/>
      <circle cx="449" cy="451" r="30"/><circle cx="401" cy="488" r="30"/><circle cx="345" cy="511" r="30"/>
      <circle cx="285" cy="519" r="30"/><circle cx="225" cy="511" r="30"/><circle cx="169" cy="488" r="30"/>
      <circle cx="121" cy="451" r="30"/><circle cx="84" cy="403" r="30"/><circle cx="61" cy="347" r="30"/>
      <circle cx="53" cy="287" r="30"/><circle cx="61" cy="227" r="30"/><circle cx="84" cy="171" r="30"/>
      <circle cx="121" cy="123" r="30"/><circle cx="169" cy="86" r="30"/><circle cx="225" cy="63" r="30"/>
    </g>
    <circle cx="285" cy="287" r="252" fill="url(#photoTone)"/>
  </svg>

  <p class="tagline">DECOMPRESS. INVIGORATE. REJUVENATE</p>
  <div class="rule rule-top"></div>
  <p class="resident">Join resident deejay <span class="dj-name">MILES HARTWICK</span></p>
  <p class="resident-link">sociallink.example/lanternsreel</p>
  <div class="rule rule-bottom"></div>

  <p class="guest-name">QUILLON</p>
  <p class="guest-details">(Special UK Garage Set starting at 6.30 pm)<br>(sociallink.example/quillon42)</p>

  <div class="venue"><span class="venue-dot"></span>CORK DEN</div>
</main>
</body>
</html>
```